Business card for a new cabinet shop company named Marlowe Cabinets for high end cabinets

Design a business card, thinking dark rich green with colours to speak of high end luxury ie; cream, gold, black possibly

Peter Lindqvar
Director Craftsman
Email: info@marlowecabinets.com.au
Instagram : @marlowe.cabinets

```html
<!DOCTYPE html>
<html lang="en">
<head>
<meta charset="UTF-8">
<title>Marlowe Cabinets — Business Card</title>
<link href="https://fonts.googleapis.com/css2?family=Inter:wght@400;600;700&display=swap" rel="stylesheet">
<style>
  :root {
    --bg-deep: #0c241b;
    --bg-mid: #123226;
    --bg-light: #173b2d;
    --panel-inner: #1d4636;
    --panel-outer: #112d22;
    --gold: #c9a95c;
    --cream: #f1ead8;
    --cream-soft: #e6dfcc;
    --badge-fill: #0f281f;
  }
  * { margin: 0; padding: 0; box-sizing: border-box; }
  html, body {
    width: 1200px;
    height: 686px;
    overflow: hidden;
    background: var(--bg-deep);
  }
  .card {
    position: relative;
    width: 1200px;
    height: 686px;
    overflow: hidden;
    font-family: "Inter", Arial, sans-serif;
    color: var(--cream);
    background: linear-gradient(90deg, var(--bg-deep) 0%, var(--bg-mid) 45%, var(--bg-light) 100%);
  }
  .card-art {
    position: absolute;
    inset: 0;
    width: 1200px;
    height: 686px;
  }
  .brand-name {
    position: absolute;
    left: 100px;
    top: 290px;
    width: 330px;
    text-align: center;
    font-weight: 600;
    font-size: 44px;
    line-height: 1.15;
    letter-spacing: 1px;
    color: var(--gold);
  }
  .contact-name,
  .contact-role,
  .contact-email,
  .contact-social {
    position: absolute;
    white-space: nowrap;
  }
  .contact-name {
    left: 546px;
    top: 76px;
    font-size: 35px;
    font-weight: 700;
    color: var(--cream);
  }
  .contact-role {
    left: 546px;
    top: 117px;
    font-size: 35px;
    font-weight: 400;
    color: var(--cream-soft);
  }
  .contact-email {
    left: 620px;
    top: 322px;
    font-size: 35px;
    font-weight: 400;
    color: var(--cream-soft);
  }
  .contact-social {
    left: 528px;
    top: 558px;
    font-size: 35px;
    font-weight: 400;
    color: var(--cream-soft);
  }
</style>
</head>
<body>
  <div class="card">
    <svg class="card-art" viewBox="0 0 1200 686" xmlns="http://www.w3.org/2000/svg" aria-hidden="true">
      <defs>
        <radialGradient id="panelShade" cx="0.42" cy="0.5" r="0.6">
          <stop offset="0" stop-color="#1d4636"/>
          <stop offset="0.7" stop-color="#163a2d"/>
          <stop offset="1" stop-color="#112d22" stop-opacity="0"/>
        </radialGradient>
        <linearGradient id="arcFade" x1="0" y1="40" x2="0" y2="646" gradientUnits="userSpaceOnUse">
          <stop offset="0" stop-color="#c9a95c" stop-opacity="0"/>
          <stop offset="0.18" stop-color="#c9a95c" stop-opacity="1"/>
          <stop offset="0.82" stop-color="#c9a95c" stop-opacity="1"/>
          <stop offset="1" stop-color="#c9a95c" stop-opacity="0"/>
        </linearGradient>
      </defs>

      <!-- left panel disc -->
      <circle class="panel-disc" cx="242" cy="343" r="326" fill="url(#panelShade)"/>
      <!-- gold arc edge, right side only -->
      <path class="panel-arc" d="M362 40 A326 326 0 0 1 362 646" fill="none" stroke="url(#arcFade)" stroke-width="6"/>

      <!-- person badge -->
      <g class="badge badge-person">
        <circle cx="475" cy="117" r="35" fill="var(--badge-fill)" stroke="#f1ead8" stroke-width="3.5"/>
        <circle cx="475" cy="108" r="8" fill="#f1ead8"/>
        <path d="M460 132 a15 13 0 0 1 30 0 z" fill="#f1ead8"/>
      </g>

      <!-- mail badge -->
      <g class="badge badge-mail">
        <circle cx="565" cy="343" r="35" fill="var(--badge-fill)" stroke="#f1ead8" stroke-width="3.5"/>
        <rect x="549" y="332" width="32" height="22" fill="none" stroke="#f1ead8" stroke-width="2.2"/>
        <path d="M549 332 L565 345 L581 332 M549 354 L560 342 M581 354 L570 342" fill="none" stroke="#f1ead8" stroke-width="2"/>
      </g>

      <!-- social handle badge: generic link icon -->
      <g class="badge badge-social">
        <circle cx="475" cy="580" r="35" fill="var(--badge-fill)" stroke="#f1ead8" stroke-width="3.5"/>
        <g fill="none" stroke="#f1ead8" stroke-width="3" stroke-linecap="round" transform="rotate(-45 475 580)">
          <rect x="457" y="573" width="20" height="14" rx="7"/>
          <rect x="473" y="573" width="20" height="14" rx="7"/>
        </g>
      </g>
    </svg>

    <div class="brand-name">Marlowe<br>Cabinets</div>

    <div class="contact-name">Peter Lindqvar</div>
    <div class="contact-role">Director Craftsman</div>
    <div class="contact-email">info@marlowecabinets.com.au</div>
    <div class="contact-social">@marlowe.cabinets</div>
  </div>
</body>
</html>
```